PLUME study results infographic

We enjoyed the previous infographic design you provided for us (The GLaRN cohort study Infographic), and would like to invite you to design another infographic in a similar style and layout.
We need an infographic which presents the results from the PLUME research trial. It should be colourful and engaging, in understandable language and showing the steps to get to the results. This is to showcase the results to patients/the public/clinicians, giving a brief summary of what the study proved. The final design should have the PLUME logo at the top (please see attached and https://plume.vextru.qb.zz.example/welcome-plume-trial)
I have attached the required logos which need to be used (PLUME, Carrowby Injury and Acute Care, University of Carrowby) as well as an example from another study, The GLaRN cohort study Infographic, as an example of what the layout could look like. Please DO NOT use the content from the The GLaRN cohort study Infographic example though, please instead use the content from the attached document 'PLUME_InfographicDesignInformation_PitchHive'.

```html
<!DOCTYPE html>
<html lang="en">
<head>
<meta charset="utf-8">
<title>PLUME study results infographic</title>
<link href="https://fonts.googleapis.com/css2?family=Montserrat:wght@400;500;600;700;800&family=Oswald:wght@500&display=swap" rel="stylesheet">
<style>
:root{
  --navy:#001c54;
  --ink:#0b1f4f;
  --cyan:#00aeef;
  --sky:#29a9e0;
  --teal:#009a96;
  --methods-bg:#d5e8f5;
  --findings-bg:#e8f4fb;
  --row-label:#b3cde0;
  --row-body:#cfe3f2;
  --royal:#2e3ec4;
  --gold:#f2b33d;
  --grey:#555a66;
  --logo-grey:#7d8590;
}
*{margin:0;padding:0;box-sizing:border-box}
html,body{width:849px;height:1200px;overflow:hidden;background:#fff}
body{font-family:'Montserrat',sans-serif;color:var(--ink);position:relative}
.abs{position:absolute}
.header{left:0;top:0;width:849px;height:247px;background:var(--navy)}
.logo-box{background:#fff;display:flex;align-items:center;justify-content:center;gap:6px;top:45px;height:73px}
.logo-box span{font-weight:700;color:var(--navy)}
.logo-box.dark{background:var(--navy);border:1px solid #fff}
.logo-box.dark span{color:#fff}
.logo-square{width:14px;height:14px;background:var(--teal)}
.title{left:20px;top:136px;width:809px;text-align:center;color:#fff;font-weight:700;font-size:19.5px;line-height:23px;letter-spacing:.2px}
.title u{text-underline-offset:3px}
.band{left:0;top:247px;width:849px;height:38px;background:var(--cyan);display:flex;align-items:center;justify-content:center;font-weight:700;font-size:13px;color:var(--navy)}
.tag{background:var(--teal);color:#fff;font-weight:700;font-size:15px;border-radius:6px;display:flex;align-items:center;justify-content:center;letter-spacing:.3px}
.summary{left:30px;top:350px;width:790px;font-size:15px;line-height:19.2px;font-weight:500}
.summary b{font-weight:800}
.methods{left:0;top:462px;width:849px;height:203px;background:var(--methods-bg)}
.design{left:33px;top:534px;font-weight:700;font-size:15px;line-height:19.2px}
.art{border-radius:4px}
.big{font-weight:800;line-height:1}
.findings{left:0;top:665px;width:849px;height:205px;background:var(--findings-bg)}
.col-head{font-weight:700;font-size:13.5px;line-height:17px;text-align:center;width:100px}
.row{left:222px;width:353px;height:59px;background:var(--row-body)}
.row-label{position:absolute;left:0;top:0;height:100%;width:113px;background:var(--row-label);clip-path:polygon(0 0,88% 0,100% 50%,88% 100%,0 100%);font-family:'Oswald',sans-serif;font-weight:500;font-size:19px;color:var(--ink);display:flex;align-items:center;padding-left:18px;letter-spacing:.5px}
.val{position:absolute;top:0;height:100%;width:100px;display:flex;align-items:center;justify-content:center;font-weight:800;font-size:31px}
.v30{left:110px;color:var(--sky)}
.v90{left:213px;color:var(--ink)}
.note{left:224px;top:849px;font-size:11px;font-weight:600}
.centered{text-align:center}
.funding{left:30px;top:1061px;width:789px;text-align:center;font-size:13.6px;line-height:19px;color:var(--grey)}
.ci-box{left:30px;top:1122px;width:310px;height:78px;background:var(--navy);color:#fff;padding:9px 16px;font-size:15px;font-weight:700;line-height:19.5px}
.ci-box .label{color:var(--cyan)}
.partner{left:362px;top:1153px;display:flex;align-items:center;gap:8px}
.partner .logo-square{width:18px;height:18px;background:#c9c9cc}
.partner span{font-size:20px;color:var(--logo-grey);font-weight:400}
</style>
</head>
<body>

<div class="abs header"></div>
<div class="abs logo-box" style="left:83px;width:217px"><div class="logo-square"></div><span style="font-size:26px;color:var(--logo-grey)">NORVELL</span></div>
<div class="abs logo-box dark" style="left:306px;width:73px;flex-direction:column;gap:0"><span style="font-size:7px;font-weight:500">UNIVERSITY OF</span><span style="font-size:11px;font-weight:500">CARROWBY</span></div>
<div class="abs logo-box" style="left:385px;width:116px"><span style="font-size:22px">PLUME</span></div>
<div class="abs logo-box" style="left:507px;width:287px"><span style="font-size:28px">NHRF</span><span style="font-size:12px;font-weight:600;line-height:14px;margin-left:6px">National Health<br>Research Fund</span></div>

<h1 class="abs title">A FEASIBILITY STUDY OF STANDARD DRESSINGS <u>VERSUS</u> NEGATIVE-PRESSURE WOUND THERAPY IN THE TREATMENT OF ADULT PATIENTS HAVING SURGICAL INCISIONS FOR HIP FRACTURES: THE PLUME RANDOMIZED CONTROLLED TRIAL</h1>

<div class="abs band">HIP FRACTURE SURGERY: CAN 'VACUUM' DRESSINGS REDUCE DEEP INFECTIONS? (FEASIBILITY TRIAL)</div>

<div class="abs tag" style="left:30px;top:297px;width:173px;height:44px">STUDY SUMMARY</div>
<p class="abs summary"><b>Adults &gt;65 years</b> undergoing hip fracture surgery at 5 UK centres were randomised to standard dressings or negative pressure 'vacuum' dressings (called iNPWT). Deep infection (CSA-defined) was assessed at 30 &amp; 90 days; other outcomes like Health Related Quality of Life were assessed at 120 days. The overall deep SSI rate was ~4%; effect signals favoured iNPWT, and a <b>definitive trial was deemed feasible.</b></p>

<section class="abs methods"></section>
<div class="abs tag" style="left:30px;top:478px;width:105px;height:43px">METHODS</div>
<p class="abs design">Two-arm<br>Multicentre<br>Randomised<br>Controlled<br>Trial</p>
<div class="abs art" role="img" aria-label="Illustration of a hospital building with a medical cross" style="left:149px;top:511px;width:124px;height:127px;background:linear-gradient(#2f48b8 0 28%,#e9eef6 28%)"></div>
<div class="abs big centered" style="left:295px;top:545px;width:60px;font-size:47px">5</div>
<div class="abs centered" style="left:285px;top:588px;width:80px;font-size:16px;line-height:16px;font-weight:500">UK<br>Centres</div>
<div class="abs" role="img" aria-label="Illustration of a die inside a circle representing randomisation" style="left:368px;top:523px;width:112px;height:112px;border-radius:50%;background:linear-gradient(90deg,#0a3366 50%,#2f3fc4 50%)"></div>
<div class="abs big" style="left:501px;top:547px;font-size:51px">462</div>
<div class="abs" style="left:502px;top:589px;font-size:17px;font-weight:500">randomized</div>
<div class="abs" style="left:642px;top:550px;font-size:15px;line-height:19.2px;font-weight:700"><span style="color:var(--cyan)">Recruitment:</span><br>Jul 2017–Feb 2018;<br>Follow-up to <span style="color:var(--cyan)">120 days</span></div>

<section class="abs findings"></section>
<div class="abs tag" style="left:39px;top:682px;width:140px;height:43px">KEY FINDINGS</div>
<div class="abs big centered" style="left:40px;top:748px;width:150px;font-size:48px">~62%</div>
<div class="abs centered" style="left:35px;top:797px;width:165px;font-size:16px;line-height:19px;font-weight:500">recruitment rate<br>of eligible cases</div>

<div class="abs col-head" style="left:332px;top:682px;color:var(--sky)">DEEP SSI<br>AT 30DAYS</div>
<div class="abs col-head" style="left:435px;top:682px">DEEP SSI<br>AT 90DAYS</div>
<div class="abs row" style="top:722px"><div class="row-label">STANDARD</div><div class="val v30">6.4%</div><div class="val v90">6.4%</div></div>
<div class="abs row" style="top:783px"><div class="row-label">INPWT</div><div class="val v30">1.9%</div><div class="val v90">2.3%</div></div>
<div class="abs" role="img" aria-label="Illustration of a stapled surgical incision on skin" style="left:535px;top:719px;width:128px;height:128px;border-radius:50%;background:radial-gradient(circle at 40% 40%,#f6c3a8,#eea183)"></div>
<div class="abs big centered" style="left:670px;top:735px;width:124px;font-size:42px">4.2%</div>
<div class="abs centered" style="left:656px;top:782px;width:160px;font-size:15px;line-height:19px;font-weight:500">Overall 30-day<br>deep SSI for hip<br>fracture population.</div>
<div class="abs note">Feasibility confirmed for a fully powered effectiveness trial.</div>

<div class="abs art" role="img" aria-label="Illustration of a nurse pushing an older patient in a wheelchair" style="left:62px;top:894px;width:127px;height:123px;background:linear-gradient(135deg,#3aa7a0,#c7d0ea 60%,#e9ecf4)"></div>
<svg class="abs" style="left:180px;top:910px" width="26" height="23" viewBox="0 0 26 23"><path d="M2 12 L9 20 L24 2" fill="none" stroke="var(--gold)" stroke-width="4" stroke-linecap="round" stroke-linejoin="round"/></svg>
<div class="abs" style="left:209px;top:914px;font-size:15px;font-weight:700">INCLUSION</div>
<div class="abs" style="left:211px;top:932px;font-size:26px;font-weight:700">&gt;65 years</div>
<div class="abs" style="left:212px;top:963px;font-size:16px;line-height:19px;font-weight:500">undergoing any surgery<br>for hip fracture.</div>

<div class="abs art" role="img" aria-label="Illustration of a hand selecting one person from a group" style="left:436px;top:870px;width:113px;height:150px;background:linear-gradient(#f5cfa0 0 45%,#e8ecf7 45%)"></div>
<div class="abs" style="left:568px;top:898px;width:100px;height:34px;background:var(--navy);color:#fff;border-radius:5px;font-weight:700;font-size:12.5px;display:flex;align-items:center;justify-content:center;letter-spacing:.3px">EXCLUSION</div>
<p class="abs" style="left:568px;top:940px;width:265px;font-size:15px;line-height:19.2px;font-weight:500"><b>Undisplaced intracapsular fracture <span style="color:var(--royal)">treated with</span> cannulated screws</b>; other factors precluding participation.</p>

<div class="abs" style="left:173px;top:1049px;width:483px;height:1px;background:var(--navy)"></div>
<p class="abs funding">Royal Guild of Surgeons of Westmarch/Brackley Medical Trust (training fellowship), NHRF Carrowby Biomedical Research Centre (infrastructure support), Halden &amp; Roe (device supply).</p>

<div class="abs ci-box"><div class="label">CHIEF INVESTIGATOR:</div><div>Elena Harcourt</div><div style="font-size:13.5px">Elena.harcourt@norvell.qb.example</div></div>
<div class="abs partner"><div class="logo-square"></div><span>CARROWBY INJURY &amp; ACUTE CARE</span></div>

</body>
</html>
```